Child sleep consultant needs a flyer to attract new clients

We need a flyer that will attract the attention of parents with children between newborn and 3 years old who may be experiencing sleep issues. The flyer will be placed at places such as community centres, doctors room, play centres, etc.

Our business is called Hushwood Nestlings and provides a sleep consultancy service. Our service essentially provides a routine for parents to follow and general advice. Our service is not medical advice.

We need the flyer to have an overall tone that is soft and peaceful however can catch the attention of parents who may be struggling on minimal sleep. We would like photos with minimal text. The colour we use is green.

We will provide the text to appear in the flyer once we have a better idea of the layout that we prefer for the flyer. The text however wont be extensive, just some catchy points.

We want to direct people to our website which is hushwoodnestlings.com.au. We also have a facebook page, which is Hushwood Nestlings.

We have a logo that we would like to appear on the flyer. We will attach the file once the uploader on pixel bazaar is fixed.

Our consultant is a certified Dream Anchor consultant, which has a separate logo that should appear somewhere on the logo. I will attach this once the uploader is fixed.

When we print the flyer - we want to print A5 SIZE ... please make sure the formatting is OK for this size.

Target Market(s)

Mums and Dads with children between newborn and 3 years old.

Industry/Entity Type

Consultant

Colors
cadf82

Requirements
Must have
• - Our logo.
• - Dream Anchor consultant logo - both attached to this brief.
• - Contact details - including phone number, email address and website
• - MUST be suitable for A5 printable size, double sided please.
• Must have the following text:
• If your baby or toddler isn't sleeping through the night, neither are you - and this means you are probably feeling physically and mentally exhausted, stressed, depressed and irritable, afraid you might be damaging your child and disconnected from your partner.
• The good news is nearly all healthy children 3 months or older are physically capable of sleeping 12 solid hours without waking. They just need to be taught the healthy sleep habits that enable them to do so.
• I can help with the sleep issues your child is experiencing. As a certified Dream Anchor (insert trademark TM here) I can help if:
• - your child will only fall asleep when nursing or bottle feeding
• - your child needs a dummy in order fall asleep
• - you're waking up with your child one or more times per night
• - your child needs to be rocked, patted, or taken for a car ride to go to sleep
• - your own lack of sleep is starting to take a toll on your family
• I've been personally trained by Marla Penwick, best selling author of the Dream Anchor (insert trade mark symbol here) Program to teach her sleep training methods to families like yours. Marla's methods have already helped over 30,000 parents and children and I'd be delighted to help your family next!
• Call or email for a free 15 minute consultation
• I would love to connect with you to talk about your child's specific situation and discuss different solutions.

```html
<!DOCTYPE html>
<html lang="en">
<head>
<meta charset="utf-8">
<title>Hushwood Nestlings – A5 Flyer</title>
<link rel="stylesheet" href="https://fonts.googleapis.com/css2?family=Oswald:wght@300&family=Pompiere&display=swap">
<style>
  :root {
    --green: #85b07a;
    --green-light: #cadf82;
    --green-pale: #dcebc0;
    --green-dark: #4f6e46;
    --green-text: #5e8453;
    --green-soft: #93bb7f;
    --white: #ffffff;
    --backdrop: #e6e6e6;
    --photo-a: #f3f0eb;
    --photo-b: #dccdbf;
    --photo-c: #efe6da;
  }
  * { box-sizing: border-box; margin: 0; padding: 0; }
  html, body { width: 1200px; height: 960px; overflow: hidden; }
  body {
    background: var(--backdrop);
    font-family: "Pompiere", sans-serif;
    position: relative;
  }
  h1, h2, p { font-weight: 400; }
  .page {
    position: absolute;
    top: 112px;
    width: 516px;
    height: 732px;
    background: var(--white);
    overflow: hidden;
    box-shadow: 0 12px 24px rgba(0,0,0,0.18);
  }
  .page--front { left: 58px; }
  .page--back { left: 623px; }
  .page svg.shapes { position: absolute; left: 0; top: 0; }
  .abs { position: absolute; }

  /* brand mark */
  .brand { display: flex; align-items: center; gap: 10px; color: var(--green-soft); }
  .brand__dot { width: 46px; height: 46px; border-radius: 50%; background: var(--green-light); flex: none; }
  .brand__name { font-size: 36px; line-height: 32px; }

  /* front */
  .front-brand { left: 24px; top: 36px; }
  .headline {
    left: 268px; top: 42px; width: 246px;
    color: var(--green-dark); font-size: 36px; line-height: 34px;
  }
  .headline span { display: block; white-space: nowrap; }
  .headline .l2 { padding-left: 32px; }
  .headline .l4 { padding-left: 80px; }
  .cta {
    left: 74px; top: 396px; width: 180px;
    font-family: "Oswald", sans-serif; font-weight: 300;
    color: var(--white); font-size: 19px; line-height: 25px; text-transform: uppercase;
  }
  .cta span { display: block; white-space: nowrap; }
  .cta .l2 { padding-left: 38px; }
  .cta .l3 { padding-left: 12px; }
  .intro {
    left: 0; top: 515px; width: 516px; text-align: center;
    color: var(--green-dark); font-size: 15px; line-height: 18.5px;
  }
  .intro span { display: block; white-space: nowrap; }
  .tagline {
    left: 0; top: 626px; width: 516px; text-align: center;
    font-family: "Oswald", sans-serif; font-weight: 300;
    color: var(--green-soft); font-size: 23px; text-transform: uppercase;
  }
  .front-contact {
    left: 0; top: 672px; width: 516px; text-align: center;
    color: var(--green-text); font-size: 25px; white-space: nowrap;
  }
  .front-contact .sep { color: var(--green-light); padding: 0 4px; }

  /* back */
  .back-heading {
    left: 0; top: 44px; width: 516px; text-align: center;
    font-family: "Oswald", sans-serif; font-weight: 300;
    color: var(--white); font-size: 19.5px; line-height: 29px; text-transform: uppercase;
  }
  .reasons { left: 0; top: 114px; width: 516px; }
  .reason {
    position: absolute; width: 90px; text-align: center;
    color: var(--white); font-size: 15px; line-height: 21px; white-space: nowrap;
  }
  .reason__star { display: block; margin: 0 auto 10px; }
  .trained {
    left: 0; top: 312px; width: 516px; text-align: center;
    color: var(--white); font-size: 15.5px; line-height: 23px; white-space: nowrap;
  }
  .results {
    left: 240px; top: 384px; width: 260px; text-align: center;
    font-family: "Oswald", sans-serif; font-weight: 300;
    color: var(--white); font-size: 15.5px; line-height: 22.5px; text-transform: uppercase;
  }
  .results span { display: block; white-space: nowrap; }
  .connect {
    left: 0; top: 502px; width: 516px; text-align: center;
    color: var(--green-dark); font-size: 25px; line-height: 30px; white-space: nowrap;
  }
  .back-brand { left: 42px; top: 612px; }
  .web {
    left: 258px; top: 589px; width: 224px; text-align: center;
    color: var(--green-dark); font-size: 19px; white-space: nowrap;
  }
  .back-contact {
    left: 240px; top: 630px; width: 250px; text-align: center;
    color: var(--green-dark); font-size: 19px; line-height: 27px; white-space: nowrap;
  }
</style>
</head>
<body>

<section class="page page--front">
  <svg class="shapes" width="516" height="732" viewBox="0 0 516 732">
    <defs>
      <linearGradient id="photoTone" x1="0" y1="0" x2="1" y2="1">
        <stop offset="0" stop-color="var(--photo-a)"/>
        <stop offset="0.5" stop-color="var(--photo-b)"/>
        <stop offset="1" stop-color="var(--photo-c)"/>
      </linearGradient>
    </defs>
    <path role="img" aria-label="Photo of a newborn baby sleeping, swaddled in a soft cream blanket"
          fill="url(#photoTone)"
          d="M0,0 H516 V400 C500,450 420,492 320,492 C220,492 150,440 80,400 C40,380 10,330 0,310 Z"/>
    <path fill="var(--white)"
          d="M0,0 H232 C250,20 252,60 236,80 C260,100 258,150 228,166 C226,196 196,210 170,200 C150,222 110,222 92,206 C70,220 30,216 0,200 Z"/>
    <path fill="var(--green)" stroke="var(--green-light)" stroke-width="2"
          d="M60,388 C56,360 90,346 110,358 C122,330 168,326 184,350 C204,332 240,348 238,376 C262,384 270,420 252,440 C266,470 240,492 214,484 L70,484 C40,484 34,448 52,432 C36,414 42,392 60,388 Z"/>
    <path fill="var(--green-light)" d="M108,366 l3,6 6,1 -4,4 1,6 -6,-3 -6,3 1,-6 -4,-4 6,-1z"/>
    <path fill="var(--green-light)" d="M126,378 l2,4 4,.5 -3,3 .7,4 -3.7,-2 -3.7,2 .7,-4 -3,-3 4,-.5z"/>
  </svg>

  <div class="abs brand front-brand">
    <span class="brand__dot"></span>
    <span class="brand__name">Hushwood<br>Nestlings</span>
  </div>

  <h1 class="abs headline">
    <span>We help families</span>
    <span class="l2">and their little ones</span>
    <span>to get the sleep</span>
    <span class="l4">they need.</span>
  </h1>

  <p class="abs cta"><span>Call or email for</span><span class="l2">a free 15 minute</span><span class="l3">consultation ✦</span></p>

  <p class="abs intro">
    <span>If your baby or toddler isn't sleeping through the night, neither are you - and this means</span>
    <span>you are probably feeling physically and mentally exhausted, stressed, depressed and irritable,</span>
    <span>afraid you might be damaging your child and disconnected from your partner. The good news is nearly all</span>
    <span>healthy children 3 months or older are physically capable of sleeping 12 solid hours without waking.</span>
    <span>They just need to be taught the healthy sleep habits that enable them to do so.</span>
  </p>

  <p class="abs tagline">Your little person is never too young to start</p>

  <p class="abs front-contact">E: wren@hushwoodnestlings.com.au <span class="sep">✦</span> P: 0400 555 127</p>
</section>

<section class="page page--back">
  <svg class="shapes" width="516" height="732" viewBox="0 0 516 732">
    <path fill="var(--green)"
          d="M0,0 H516 V420 C524,470 480,492 440,488 L290,488 C250,492 230,460 240,430 C250,400 230,380 208,390 C190,370 150,372 140,380 C120,364 80,366 66,380 C40,360 30,330 32,310 C18,300 6,298 0,300 Z"/>
    <path fill="none" stroke="var(--white)" stroke-width="1.3" stroke-dasharray="5 4"
          d="M0,226 C60,236 110,250 150,262 C180,272 180,290 160,294 C140,290 140,266 168,262 C220,262 260,280 290,286 C300,290 296,280 290,276 C282,270 280,284 300,290 C360,300 400,280 440,270 C480,266 500,280 516,308"/>
    <path fill="var(--white)" stroke="var(--green-light)" stroke-width="2"
          d="M62,470 C38,470 32,440 52,430 C44,406 68,394 86,404 C94,382 128,378 142,396 C160,386 186,400 180,422 C196,430 194,464 172,470 Z"/>
    <path fill="var(--green-light)" d="M196,472 l4,8 8,1 -6,6 1.5,8 -7.5,-4 -7.5,4 1.5,-8 -6,-6 8,-1z"/>
    <path fill="var(--green-light)" d="M214,482 l2,4 4,.5 -3,3 .7,4 -3.7,-2 -3.7,2 .7,-4 -3,-3 4,-.5z"/>
    <path fill="var(--green-light)" d="M236,470 C226,462 222,450 232,448 C238,446 240,452 240,452 C242,446 250,446 252,452 C254,460 244,466 236,470 Z"/>
    <path fill="var(--green-light)" d="M450,565 l2,4 4,.5 -3,3 .7,4 -3.7,-2 -3.7,2 .7,-4 -3,-3 4,-.5z"/>
    <path fill="var(--green-pale)" d="M242,584 H492 L482,601 L492,618 H242 L250,601 Z"/>
  </svg>

  <h2 class="abs back-heading">I can help with the sleep issues your child is experiencing.<br>As a certified Dream Anchor™ I can help if:</h2>

  <div class="abs reasons">
    <p class="reason" style="left:37px"><svg class="reason__star" width="16" height="16" viewBox="0 0 16 16"><path fill="var(--green-light)" d="M8,0 l2.4,5 5.6,.8 -4,3.9 1,5.5 -5,-2.6 -5,2.6 1,-5.5 -4,-3.9 5.6,-.8z"/></svg>your child will<br>only fall asleep<br>when nursing or<br>bottle feeding</p>
    <p class="reason" style="left:128px"><svg class="reason__star" width="16" height="16" viewBox="0 0 16 16"><path fill="var(--green-light)" d="M8,0 l2.4,5 5.6,.8 -4,3.9 1,5.5 -5,-2.6 -5,2.6 1,-5.5 -4,-3.9 5.6,-.8z"/></svg>your child needs<br>a dummy<br>in order<br>fall asleep</p>
    <p class="reason" style="left:218px"><svg class="reason__star" width="16" height="16" viewBox="0 0 16 16"><path fill="var(--green-light)" d="M8,0 l2.4,5 5.6,.8 -4,3.9 1,5.5 -5,-2.6 -5,2.6 1,-5.5 -4,-3.9 5.6,-.8z"/></svg>you're waking<br>up with your<br>child one<br>or more times<br>per night</p>
    <p class="reason" style="left:308px"><svg class="reason__star" width="16" height="16" viewBox="0 0 16 16"><path fill="var(--green-light)" d="M8,0 l2.4,5 5.6,.8 -4,3.9 1,5.5 -5,-2.6 -5,2.6 1,-5.5 -4,-3.9 5.6,-.8z"/></svg>your child needs<br>to be rocked,<br>patted, or taken<br>for a car ride to<br>go to sleep your<br>own lack of</p>
    <p class="reason" style="left:398px"><svg class="reason__star" width="16" height="16" viewBox="0 0 16 16"><path fill="var(--green-light)" d="M8,0 l2.4,5 5.6,.8 -4,3.9 1,5.5 -5,-2.6 -5,2.6 1,-5.5 -4,-3.9 5.6,-.8z"/></svg>sleep is starting<br>to take a toll<br>on your family</p>
  </div>

  <p class="abs trained">I've been personally trained by Marla Penwick, best selling author of<br>the Dream Anchor™ Program to teach her sleep training methods to families like yours.</p>

  <p class="abs results">
    <span>Marla's methods have already helped</span>
    <span>over 30,000 parents and children</span>
    <span>and I'd be delighted to help</span>
    <span>your family next!</span>
  </p>

  <p class="abs connect">I would love to connect with you to talk about your child's<br>specific situation and discuss different solutions.</p>

  <div class="abs brand back-brand">
    <span class="brand__dot"></span>
    <span class="brand__name">Hushwood<br>Nestlings</span>
  </div>

  <p class="abs web">www.hushwoodnestlings.com.au</p>
  <p class="abs back-contact">E: wren@hushwoodnestlings.com.au<br>P: 0400 555 127<br>facebook.com/hushwoodnestlings</p>
</section>

</body>
</html>
```